Business card, invoice design and email signature for accounting firm
Tallyworks.Ca
Business card, invoice design and email signature for accounting firm - Financial Services
Creative Brief
Simple
Marta Elkins, BA, CGA
Certified General Accountant
47 Wexmoor Lane Dorchester, ON N0L2H5
marta@tallyworks.ca
www.tallyworks.ca
we don't need the letterhead and envelope.

```html
<!DOCTYPE html>
<html lang="en">
<head>
<meta charset="utf-8">
<title>Tallyworks.Ca Stationery</title>
<link href="https://fonts.googleapis.com/css2?family=Nunito:wght@400;700;800&display=swap" rel="stylesheet">
<style>
:root{
  --purple:#5b2d8e;
  --green:#8cc63f;
  --paper:#ffffff;
  --ink:#3a3a3a;
  --rule:#c9c9c9;
  --backdrop:#ecebe8;
}
*{box-sizing:border-box;margin:0;padding:0}
html,body{width:1200px;height:974px;overflow:hidden}
body{background:var(--backdrop);font-family:"Nunito",sans-serif;color:var(--ink);position:relative}
.sheet{position:absolute;background:var(--paper);box-shadow:0 2px 8px rgba(0,0,0,.18);overflow:hidden}
.invoice-a{left:105px;top:79px;width:295px;height:368px}
.invoice-b{left:105px;top:500px;width:295px;height:381px}
.letter-a{left:500px;top:79px;width:295px;height:389px}
.letter-b{left:500px;top:500px;width:295px;height:381px}
.card-white{left:881px;top:271px;width:224px;height:130px;border-radius:8px}
.card-green{left:881px;top:368px;width:224px;height:132px;border-radius:8px;background:var(--green);top:368px}
.sig-a{left:881px;top:558px;width:224px;height:73px}
.sig-b{left:881px;top:689px;width:224px;height:61px}
.card-white{top:240px;height:118px}
.card-green{top:372px;height:124px}
.logo{display:flex;align-items:center;gap:4px;font-weight:800;color:var(--purple);font-size:12px;white-space:nowrap}
.logo .mark{width:9px;height:9px;background:var(--green);border-radius:50%}
.logo-top{position:absolute;top:10px;right:22px}
.logo-center{position:absolute;top:12px;left:50%;transform:translateX(-50%)}
.wave{position:absolute;left:0;bottom:0;width:100%;height:58px}
.invoice-title{position:absolute;left:14px;top:18px;font-weight:800;font-size:10px;letter-spacing:.5px}
.meta{position:absolute;font-size:5px;color:#666}
.bill{left:14px;top:34px}
.date{right:22px;top:42px;text-align:right;line-height:1.6}
.table{position:absolute;left:14px;top:64px;width:250px;border-collapse:collapse;font-size:4.5px}
.table th{border:1px solid var(--rule);font-weight:700;padding:2px;text-align:center;background:#f4f4f4}
.table td{border-left:1px solid var(--rule);border-right:1px solid var(--rule);height:9px}
.table tr:last-child td{border-bottom:1px solid var(--rule)}
.totals{position:absolute;right:31px;width:72px;font-size:4.5px;border-collapse:collapse}
.totals td{border:1px solid var(--rule);padding:2px;height:9px}
.note{position:absolute;left:14px;font-size:5px;font-weight:700;line-height:1.4}
.footer-text{position:absolute;right:12px;bottom:8px;font-size:4.5px;color:#fff;text-align:right;line-height:1.45}
.card-info{position:absolute;right:12px;top:10px;font-size:5px;text-align:right;line-height:1.5}
.card-info strong{font-size:6px;color:var(--purple)}
.green-panel{position:absolute;left:50%;top:18px;transform:translateX(-50%);background:#fff;border-radius:6px;padding:8px 14px}
.green-contact{position:absolute;left:0;right:0;bottom:0;height:20px;background:var(--purple);color:#fff;font-size:5px;display:flex;align-items:center;justify-content:center;gap:16px}
.sig-info{position:absolute;right:10px;top:8px;font-size:4.5px;text-align:right;line-height:1.5}
.sig-info strong{color:var(--purple);font-size:5.5px}
</style>
</head>
<body>

<!-- Invoice, purple -->
<section class="sheet invoice-a">
  <div class="logo logo-top"><span class="mark"></span>Tallyworks.Ca</div>
  <h1 class="invoice-title">INVOICE</h1>
  <p class="meta bill">Bill To:</p>
  <p class="meta date">Date:<br>Invoice #:</p>
  <table class="table">
    <tr><th style="width:60%">Description</th><th>Qty</th><th>Rate</th><th>Amount</th></tr>
    <tr><td></td><td></td><td></td><td></td></tr><tr><td></td><td></td><td></td><td></td></tr>
    <tr><td></td><td></td><td></td><td></td></tr><tr><td></td><td></td><td></td><td></td></tr>
    <tr><td></td><td></td><td></td><td></td></tr><tr><td></td><td></td><td></td><td></td></tr>
    <tr><td></td><td></td><td></td><td></td></tr><tr><td></td><td></td><td></td><td></td></tr>
    <tr><td></td><td></td><td></td><td></td></tr><tr><td></td><td></td><td></td><td></td></tr>
  </table>
  <table class="totals" style="top:184px"><tr><td>Subtotal</td></tr><tr><td>HST</td></tr><tr><td>Total</td></tr></table>
  <p class="note" style="top:232px">Make all cheques payable to Tallyworks.Ca<br>Thank you for your business</p>
  <svg class="wave" viewBox="0 0 300 60" preserveAspectRatio="none" aria-hidden="true">
    <path d="M0 32 C90 6 190 48 300 12 L300 60 L0 60Z" fill="var(--purple)"/>
    <path d="M0 26 C90 0 190 42 300 6" fill="none" stroke="var(--green)" stroke-width="3"/>
  </svg>
  <p class="footer-text">Marta Elkins<br>47 Wexmoor Lane Dorchester, ON N0L2H5<br>Tel 519 555 0142<br>www.tallyworks.ca</p>
</section>

<!-- Letterhead, purple -->
<section class="sheet letter-a">
  <div class="logo logo-center"><span class="mark"></span>Tallyworks.Ca</div>
  <svg class="wave" viewBox="0 0 300 60" preserveAspectRatio="none" aria-hidden="true">
    <path d="M0 32 C90 6 190 48 300 12 L300 60 L0 60Z" fill="var(--purple)"/>
    <path d="M0 26 C90 0 190 42 300 6" fill="none" stroke="var(--green)" stroke-width="3"/>
  </svg>
  <p class="footer-text">Marta Elkins<br>47 Wexmoor Lane Dorchester, ON N0L2H5<br>Tel 519 555 0142<br>www.tallyworks.ca</p>
</section>

<!-- Business card, white side -->
<section class="sheet card-white">
  <div class="card-info"><strong>Marta Elkins, BA, CGA</strong><br>Certified General Accountant</div>
  <div class="logo" style="position:absolute;left:14px;top:44px;font-size:14px"><span class="mark"></span>Tallyworks.Ca</div>
  <svg class="wave" viewBox="0 0 300 60" preserveAspectRatio="none" aria-hidden="true" style="height:44px">
    <path d="M0 34 C90 8 190 46 300 14 L300 60 L0 60Z" fill="var(--purple)"/>
    <path d="M0 28 C90 2 190 40 300 8" fill="none" stroke="var(--green)" stroke-width="3"/>
  </svg>
  <p class="footer-text" style="bottom:5px">47 Wexmoor Lane Dorchester, ON N0L2H5<br>Tel 519 555 0142 &nbsp; marta@tallyworks.ca</p>
</section>

<!-- Business card, green side -->
<section class="sheet card-green">
  <div class="green-panel"><div class="logo" style="font-size:14px"><span class="mark"></span>Tallyworks.Ca</div></div>
  <div class="green-contact"><span>www.tallyworks.ca</span><span>marta@tallyworks.ca</span></div>
</section>

<!-- Invoice, green -->
<section class="sheet invoice-b">
  <div class="logo logo-top"><span class="mark"></span>Tallyworks.Ca</div>
  <h1 class="invoice-title">INVOICE</h1>
  <p class="meta bill">Bill To:</p>
  <p class="meta date">Date:<br>Invoice #:</p>
  <table class="table">
    <tr><th style="width:60%">Description</th><th>Qty</th><th>Rate</th><th>Amount</th></tr>
    <tr><td></td><td></td><td></td><td></td></tr><tr><td></td><td></td><td></td><td></td></tr>
    <tr><td></td><td></td><td></td><td></td></tr><tr><td></td><td></td><td></td><td></td></tr>
    <tr><td></td><td></td><td></td><td></td></tr><tr><td></td><td></td><td></td><td></td></tr>
    <tr><td></td><td></td><td></td><td></td></tr><tr><td></td><td></td><td></td><td></td></tr>
    <tr><td></td><td></td><td></td><td></td></tr><tr><td></td><td></td><td></td><td></td></tr>
  </table>
  <table class="totals" style="top:184px"><tr><td>Subtotal</td></tr><tr><td>HST</td></tr><tr><td>Total</td></tr></table>
  <p class="note" style="top:240px">Make all cheques payable to Tallyworks.Ca<br>Thank you for your business</p>
  <svg class="wave" viewBox="0 0 300 60" preserveAspectRatio="none" aria-hidden="true">
    <path d="M0 32 C90 6 190 48 300 12 L300 60 L0 60Z" fill="var(--green)"/>
    <path d="M0 26 C90 0 190 42 300 6" fill="none" stroke="var(--purple)" stroke-width="3"/>
  </svg>
  <p class="footer-text">Marta Elkins<br>47 Wexmoor Lane Dorchester, ON N0L2H5<br>Tel 519 555 0142<br>www.tallyworks.ca</p>
</section>

<!-- Letterhead, green -->
<section class="sheet letter-b">
  <div class="logo logo-center"><span class="mark"></span>Tallyworks.Ca</div>
  <svg class="wave" viewBox="0 0 300 60" preserveAspectRatio="none" aria-hidden="true">
    <path d="M0 32 C90 6 190 48 300 12 L300 60 L0 60Z" fill="var(--green)"/>
    <path d="M0 26 C90 0 190 42 300 6" fill="none" stroke="var(--purple)" stroke-width="3"/>
  </svg>
  <p class="footer-text">Marta Elkins<br>47 Wexmoor Lane Dorchester, ON N0L2H5<br>Tel 519 555 0142<br>www.tallyworks.ca</p>
</section>

<!-- Email signature, purple -->
<section class="sheet sig-a">
  <div class="logo" style="position:absolute;left:10px;top:14px;font-size:11px"><span class="mark"></span>Tallyworks.Ca</div>
  <div class="sig-info"><strong>Marta Elkins, BA, CGA</strong><br>Certified General Accountant<br>Tel 519 555 0142</div>
  <svg class="wave" viewBox="0 0 300 60" preserveAspectRatio="none" aria-hidden="true" style="height:22px">
    <path d="M0 34 C90 8 190 46 300 14 L300 60 L0 60Z" fill="var(--purple)"/>
    <path d="M0 26 C90 0 190 40 300 6" fill="none" stroke="var(--green)" stroke-width="4"/>
  </svg>
</section>

<!-- Email signature, green -->
<section class="sheet sig-b">
  <div class="logo" style="position:absolute;left:10px;top:12px;font-size:11px"><span class="mark"></span>Tallyworks.Ca</div>
  <div class="sig-info"><strong>Marta Elkins, BA, CGA</strong><br>marta@tallyworks.ca<br>Tel 519 555 0142</div>
  <svg class="wave" viewBox="0 0 300 60" preserveAspectRatio="none" aria-hidden="true" style="height:18px">
    <path d="M0 34 C90 8 190 46 300 14 L300 60 L0 60Z" fill="var(--green)"/>
    <path d="M0 26 C90 0 190 40 300 6" fill="none" stroke="var(--purple)" stroke-width="4"/>
  </svg>
</section>

</body>
</html>
```